Herbal tea shop web designing - Leafwell

We need a business-charity purpose online shop selling premium herbal teas with a tagline "Healthy with a heart" where all the raw materials are being purchased from Indonesian local farmers in order to give them sustainable employment. Every 20% from the total amount of the customer's purchase from our website always goes back to their communities to help build better sanitation, education or whatever they need. We need page to blog too and another page for customers to interact and share their thought. we expect an eye catching simple earthy (maybe a bit rustic) design with some brush lettering font in some parts. Thank you.

Target Market(s)

-Tea Lovers
-Anyone with body weight issues or any health issues in general

Industry/Entity Type

Home Health Care

Number of Pages Required

5+ page

Font styles to use
Other font styles liked:
• brush lettering font in some parts

Requirements
Must have
• - Brush lettering font
• -Simple, a bit rustic design with some nice watercolor touch
• -Blogging Page
• -catchy yet fancy and elegant E-commerce page
Nice to have
• Well, I will let the designers use their skills and imaginations to the fullest.

```html
<!DOCTYPE html>
<html lang="en">
<head>
<meta charset="utf-8">
<title>Leafwell – Healthy with a heart</title>
<link rel="stylesheet" href="https://fonts.googleapis.com/css2?family=Allura&family=Roboto:wght@400;500;700&display=swap">
<style>
  :root {
    --ink: #2b2724;
    --muted: #8a8580;
    --white: #ffffff;
    --sand: #efebe8;
    --green: #1f9d5c;
    --footer: #38332f;
    --footer-text: #d8d3ce;
    --line: #e6e2de;
    --script: "Allura", cursive;
    --sans: "Roboto", Arial, sans-serif;
  }
  * { box-sizing: border-box; margin: 0; padding: 0; }
  html, body { width: 1200px; height: 2406px; overflow: hidden; }
  body { font-family: var(--sans); color: var(--ink); background: var(--white); position: relative; }

  /* Hero */
  .hero { position: absolute; left: 0; top: 0; width: 1200px; height: 533px;
    background: linear-gradient(100deg, #b9b2a8 0%, #d8d2ca 25%, #efe9e2 45%, #cdbfae 62%, #6e5b4b 85%, #4a3e35 100%); }
  .hero-nav { position: absolute; top: 33px; left: 88px; display: flex; gap: 26px; font-size: 11px; font-weight: 500; color: var(--white); letter-spacing: .3px; }
  .hero-nav .active { position: relative; }
  .hero-nav .active::before { content: ""; position: absolute; top: -33px; left: 0; width: 32px; height: 3px; background: var(--white); }
  .logo { position: absolute; top: 29px; left: 0; width: 1200px; text-align: center; font-weight: 700; font-size: 16px; color: var(--white); }
  .hero-tools { position: absolute; top: 33px; right: 88px; display: flex; gap: 18px; font-size: 11px; color: var(--white); align-items: center; }
  .hero-tools span { display: flex; align-items: center; gap: 5px; }
  .tagline { position: absolute; top: 222px; width: 1200px; text-align: center; font-family: var(--script); font-weight: 400; font-size: 84px; color: var(--white); line-height: 1; }
  .shop-now { position: absolute; top: 325px; left: 550px; display: flex; align-items: center; gap: 10px; font-size: 11px; color: var(--white); letter-spacing: .5px; }
  .shop-now i { width: 24px; height: 24px; border-radius: 50%; background: rgba(255,255,255,.3); display: flex; align-items: center; justify-content: center; }

  /* Section headings */
  .script-title { position: absolute; width: 1200px; left: 0; text-align: center; font-family: var(--script); font-weight: 400; font-size: 42px; line-height: 1; color: var(--ink); }
  .subtitle { position: absolute; width: 1200px; left: 0; text-align: center; font-size: 12px; color: var(--muted); }

  /* Charity */
  .charity-text { position: absolute; top: 648px; left: 220px; width: 760px; text-align: center; font-size: 12.5px; line-height: 22px; color: var(--muted); }
  .feature { position: absolute; top: 736px; width: 493px; height: 259px; overflow: hidden; }
  .feature.teas { left: 88px; background: linear-gradient(120deg, #4a5260 0%, #7a6a5a 45%, #b08a66 100%); }
  .feature.shop { left: 618px; background: linear-gradient(120deg, #3b3634 0%, #9c8373 45%, #e4b36e 100%); }
  .feature h3 { position: absolute; left: 38px; bottom: 34px; font-size: 21px; font-weight: 700; color: var(--white); }
  .feature .go { position: absolute; right: 22px; bottom: 30px; width: 26px; height: 26px; border-radius: 50%; background: rgba(255,255,255,.3); display: flex; align-items: center; justify-content: center; }

  /* Products */
  .products { position: absolute; top: 1070px; left: 0; width: 1200px; height: 547px; background: var(--sand); }
  .product-row { position: absolute; top: 1210px; left: 88px; width: 1022px; height: 282px; background: var(--white); }
  .product { position: absolute; top: 1210px; width: 255px; height: 282px; }
  .product + .product { border-left: 1px solid var(--line); }
  .product.raised { top: 1205px; left: 595px; width: 265px; height: 293px; background: var(--white); box-shadow: 0 10px 30px rgba(0,0,0,.12); z-index: 2; border: none; }
  .pack { position: absolute; left: 50%; transform: translateX(-50%); top: 34px; width: 112px; height: 132px; border-radius: 8px 8px 4px 4px; background: linear-gradient(90deg, #a97a4c, #c99c6b 50%, #a57546); box-shadow: 0 14px 14px -10px rgba(0,0,0,.35); }
  .pack.md { width: 94px; height: 116px; top: 52px; }
  .raised .pack { background: linear-gradient(90deg, #dbc8b0, #eee0cd 50%, #d6c2a8); }
  .product .name { position: absolute; left: 33px; top: 228px; font-size: 13px; font-weight: 500; }
  .product .price { position: absolute; left: 33px; top: 246px; font-size: 12px; font-weight: 500; color: var(--green); }
  .raised .name { top: 233px; }
  .raised .price { top: 252px; }
  .actions { position: absolute; top: 118px; left: 72px; display: flex; gap: 12px; }
  .actions i { width: 32px; height: 32px; border-radius: 50%; background: var(--ink); display: flex; align-items: center; justify-content: center; }
  .actions i.cart { background: var(--green); }
  .btn-shop { position: absolute; top: 1537px; left: 540px; width: 120px; height: 38px; border: 1px solid #cfc9c3; border-radius: 20px; font-size: 11px; font-weight: 500; display: flex; align-items: center; justify-content: center; letter-spacing: .4px; color: var(--ink); }

  /* Gallery */
  .gallery { position: absolute; top: 1768px; left: 88px; width: 1022px; height: 272px; display: grid; grid-template-columns: 173px 172px 334px 171px 172px; grid-template-rows: 136px 136px; }
  .gallery .tile.wide { grid-column: 3; grid-row: 1 / span 2; position: relative; }
  .gallery .tile.wide .cap { position: absolute; top: 128px; width: 100%; text-align: center; color: var(--white); font-size: 12px; }

  /* Footer */
  .footer { position: absolute; top: 2117px; left: 0; width: 1200px; height: 289px; background: var(--footer); color: var(--footer-text); }
  .footer h4 { font-size: 16px; font-weight: 400; color: var(--white); margin-bottom: 16px; }
  .footer .col { position: absolute; top: 50px; font-size: 12px; line-height: 22px; }
  .footer ul { list-style: none; }
  .footer li { display: flex; align-items: center; gap: 8px; }
  .pay-name { margin-top: 10px; font-weight: 700; font-size: 14px; color: var(--white); }
  .footer .rule { position: absolute; top: 240px; left: 88px; width: 1022px; height: 1px; background: rgba(255,255,255,.08); }
  .footer .copy { position: absolute; top: 257px; left: 88px; font-size: 11.5px; }
  .to-top { position: absolute; top: 2335px; left: 1135px; width: 40px; height: 40px; border-radius: 50%; background: var(--green); display: flex; align-items: center; justify-content: center; }
  .dot { width: 8px; height: 8px; border-radius: 2px; background: var(--footer-text); }
</style>
</head>
<body>

<header class="hero" role="img" aria-label="Photo of a smiling woman on the phone holding a cup of tea in a cafe">
  <nav class="hero-nav"><span class="active">HOME</span><span>SHOP</span><span>BLOGS</span><span>TESTIMONIALS</span></nav>
  <div class="logo">Leafwell</div>
  <div class="hero-tools">
    <span><svg width="13" height="12" viewBox="0 0 24 22"><path d="M12 21 3 12a5.5 5.5 0 0 1 9-7 5.5 5.5 0 0 1 9 7z" fill="none" stroke="#fff" stroke-width="2.4"/></svg>WISHLIST ▾</span>
    <span><svg width="11" height="13" viewBox="0 0 20 24"><rect x="2" y="7" width="16" height="15" fill="none" stroke="#fff" stroke-width="2"/><path d="M6 7V5a4 4 0 0 1 8 0v2" fill="none" stroke="#fff" stroke-width="2"/></svg>0 ITEMS ▾</span>
  </div>
  <h1 class="tagline">Healthy with a heart</h1>
  <div class="shop-now"><i><svg width="8" height="8" viewBox="0 0 10 10"><path d="M3 1l4 4-4 4" fill="none" stroke="#fff" stroke-width="1.6"/></svg></i>SHOP NOW</div>
</header>

<h2 class="script-title" style="top:598px">About our charity program</h2>
<p class="charity-text">Every 20% from the total amount of the customer's purchase from our website always goes back to farmers communities to help build better sanitation, education or whatever they need.</p>

<a class="feature teas" role="img" aria-label="Photo of a man working on a laptop beside a cup of tea">
  <h3>Herbal teas</h3>
  <span class="go"><svg width="8" height="8" viewBox="0 0 10 10"><path d="M3 1l4 4-4 4" fill="none" stroke="#fff" stroke-width="1.6"/></svg></span>
</a>
<a class="feature shop" role="img" aria-label="Photo of two women chatting over tea in a cafe">
  <h3>Tea Shop</h3>
  <span class="go"><svg width="8" height="8" viewBox="0 0 10 10"><path d="M3 1l4 4-4 4" fill="none" stroke="#fff" stroke-width="1.6"/></svg></span>
</a>

<section class="products"></section>
<h2 class="script-title" style="top:1116px">Our Products</h2>
<p class="subtitle" style="top:1164px">Also check more products in our shop page.</p>

<div class="product-row"></div>
<div class="product" style="left:88px">
  <div class="pack" role="img" aria-label="Kraft paper tea pouch"></div>
  <div class="name">Large pack</div><div class="price">$ 254.00</div>
</div>
<div class="product" style="left:343px">
  <div class="pack md" role="img" aria-label="Medium kraft paper tea pouch"></div>
  <div class="name">Medium Pack</div><div class="price">$ 254.00</div>
</div>
<div class="product" style="left:855px">
  <div class="pack" role="img" aria-label="Kraft paper tea pouch"></div>
  <div class="name">Large pack</div><div class="price">$ 254.00</div>
</div>
<div class="product raised">
  <div class="pack" role="img" aria-label="Light paper tea pouch"></div>
  <div class="actions">
    <i><svg width="13" height="13" viewBox="0 0 24 24"><path d="M10 14a5 5 0 0 0 7 0l3-3a5 5 0 0 0-7-7l-1 1M14 10a5 5 0 0 0-7 0l-3 3a5 5 0 0 0 7 7l1-1" fill="none" stroke="#fff" stroke-width="2.4"/></svg></i>
    <i><svg width="13" height="12" viewBox="0 0 24 22"><path d="M12 21 3 12a5.5 5.5 0 0 1 9-7 5.5 5.5 0 0 1 9 7z" fill="none" stroke="#fff" stroke-width="2.4"/></svg></i>
    <i class="cart"><svg width="14" height="13" viewBox="0 0 24 22"><path d="M1 2h4l3 12h12l2-8H6" fill="none" stroke="#fff" stroke-width="2.2"/><circle cx="9" cy="19" r="2" fill="#fff"/><circle cx="18" cy="19" r="2" fill="#fff"/></svg></i>
  </div>
  <div class="name">Large pack</div><div class="price">$ 254.00</div>
</div>
<a class="btn-shop">GO TO SHOP</a>

<h2 class="script-title" style="top:1674px">Snapgram Gallery</h2>
<p class="subtitle" style="top:1723px">Follow us on snapgram for latest updates.</p>
<div class="gallery">
  <div class="tile" role="img" aria-label="Tea press with lemons" style="background:linear-gradient(135deg,#6b5640,#b99a63)"></div>
  <div class="tile" role="img" aria-label="Blooming tea in glass pot" style="background:linear-gradient(135deg,#3d2e22,#a26e3a)"></div>
  <div class="tile wide" role="img" aria-label="Tea leaves drying in baskets on a farm" style="background:linear-gradient(160deg,#7a7a6a,#4f5a3a 55%,#3a4526)">
    <div class="cap">Also chek our snapgram gallery</div>
  </div>
  <div class="tile" role="img" aria-label="Breakfast bowl and watch on table" style="background:linear-gradient(135deg,#2e3438,#6a5a4c)"></div>
  <div class="tile" role="img" aria-label="Hands in knit sleeves holding tea" style="background:linear-gradient(135deg,#8a3a3a,#c8b8b0)"></div>
  <div class="tile" role="img" aria-label="Tea cups on wooden tray" style="background:linear-gradient(135deg,#7a5230,#c08a50)"></div>
  <div class="tile" role="img" aria-label="Tea set on dark table" style="background:linear-gradient(135deg,#2a2420,#7a5a3a)"></div>
  <div class="tile" role="img" aria-label="Flowers, photos and coffee cup" style="background:linear-gradient(135deg,#3a3530,#c8c4bc)"></div>
  <div class="tile" role="img" aria-label="Cup of tea with waffles" style="background:linear-gradient(135deg,#2a3a24,#a07850)"></div>
</div>

<footer class="footer">
  <div class="col" style="left:88px;width:340px">
    <h4>About Us</h4>
    <p>Lorem ipsum dolor sit amet, consectetuer adipiscing elit.<br>Aenean commodo ligula eget dolor aenean massa.<br>Cum sociis natoque penatibus .</p>
    <p class="pay-name">Paywise</p>
  </div>
  <div class="col" style="left:488px">
    <h4>Informations</h4>
    <ul><li>About us</li><li>Sitemap</li><li>Advanced Search</li><li>Orders and Returns</li><li>Contact</li></ul>
  </div>
  <div class="col" style="left:720px">
    <h4>My Account</h4>
    <ul><li>Log In</li><li>View Shopping Cart</li><li>My wish list</li><li>Track My Order</li><li>Help</li></ul>
  </div>
  <div class="col" style="left:938px">
    <h4>Follow us</h4>
    <ul><li><span class="dot"></span>Facenote</li><li><span class="dot"></span>Chirper</li><li><span class="dot"></span>Searchly +</li><li><span class="dot"></span>Snapgram</li></ul>
  </div>
  <div class="rule"></div>
  <p class="copy">© 2017, All Rights Reserved.</p>
</footer>
<a class="to-top"><svg width="14" height="14" viewBox="0 0 14 14"><path d="M7 12V2M3 6l4-4 4 4" fill="none" stroke="#fff" stroke-width="1.8"/></svg></a>

</body>
</html>
```